Road Construction Company needs business cards

We would like a new business card designed for our business.

We're a road construction company based in Qld, Australia.

Can the business card please have the following information on it.

Name: Brent Malvoy
Position: General Manager
Phone: 0471 592 304
Email: Brent.malvoy@quendix.com.au
Address: 87 Harrowgate Ave, Pindarra, QLD, 4000
Website: www.quendix.com.au

Visually we'd like the card to be professional and simple.

Attached is our logo.

Our website is www.quendix.com.au

Target Market(s)

Men aged 25-60

Contact Information for Business Card

As listed in project description

Font styles to use
Serif

Requirements
Must have
• Large logo on back of card

```html
<!DOCTYPE html>
<html lang="en">
<head>
<meta charset="utf-8">
<title>Quendix Business Card</title>
<link rel="stylesheet" href="https://fonts.googleapis.com/css2?family=Cinzel:wght@400;600;700&display=swap">
<style>
  :root {
    --backdrop: #9a9b9f;
    --card-dark: #000000;
    --card-light: #ffffff;
    --brand-blue: #1057a8;
    --accent-blue: #2aa5dc;
    --ink: #111111;
    --rule: #333333;
  }
  * { margin: 0; padding: 0; box-sizing: border-box; }
  html, body { width: 988px; height: 1200px; overflow: hidden; }
  body {
    background: var(--backdrop);
    font-family: "Cinzel", serif;
    color: var(--ink);
    position: relative;
  }
  .card {
    position: absolute;
    box-shadow: 3px 4px 8px rgba(0,0,0,0.35);
    overflow: hidden;
  }
  .card--front {
    left: 73px; top: 89px; width: 840px; height: 476px;
    background: var(--card-dark);
    display: flex; align-items: center; justify-content: center;
  }
  .card--back {
    left: 74px; top: 627px; width: 841px; height: 478px;
    background: var(--card-light);
  }
  .brand-name {
    font-family: "Cinzel", serif;
    font-weight: 700;
    color: var(--brand-blue);
    letter-spacing: 0.02em;
    line-height: 1;
  }
  .card--front .brand-name { font-size: 104px; margin-top: -40px; }
  .card--back .brand-name {
    position: absolute; left: 0; right: 0; top: 47px;
    text-align: center; font-size: 70px;
  }
  .holder {
    position: absolute; left: 44px; width: 330px; top: 242px;
    text-align: center;
  }
  .holder__name { font-size: 34px; font-weight: 600; line-height: 1; }
  .holder__role { font-size: 17px; font-weight: 600; margin-top: 10px; }
  .divider {
    position: absolute; left: 379px; top: 190px; width: 1px; height: 199px;
    background: var(--rule);
  }
  .contact {
    position: absolute; left: 420px; top: 200px;
    font-size: 17px; font-weight: 400;
  }
  .contact__address p { line-height: 36px; }
  .contact__list { list-style: none; margin-top: 17px; }
  .contact__list li {
    display: flex; align-items: center; height: 33px; font-size: 17px;
  }
  .contact__list li.small { font-size: 15.5px; }
  .contact__list svg { width: 17px; height: 17px; margin-right: 14px; flex: none; }
  .card__bands {
    position: absolute; left: 0; bottom: 0; width: 841px; height: 32px;
  }
</style>
</head>
<body>
  <section class="card card--front">
    <div class="brand-name">QUENDIX</div>
  </section>

  <section class="card card--back">
    <div class="brand-name">QUENDIX</div>

    <div class="holder">
      <p class="holder__name">Brent Malvoy</p>
      <p class="holder__role">GENERAL MANAGER</p>
    </div>

    <div class="divider"></div>

    <div class="contact">
      <div class="contact__address">
        <p>87 Harrowgate Ave,</p>
        <p>Pindarra, QLD, 4000</p>
      </div>
      <ul class="contact__list">
        <li>
          <svg viewBox="0 0 24 24" aria-hidden="true"><path fill="#111" d="M6.6 10.8a15.1 15.1 0 0 0 6.6 6.6l2.2-2.2c.3-.3.7-.4 1-.2 1.1.4 2.3.6 3.6.6.6 0 1 .4 1 1V20c0 .6-.4 1-1 1A17 17 0 0 1 3 4c0-.6.4-1 1-1h3.5c.6 0 1 .4 1 1 0 1.3.2 2.5.6 3.6.1.3 0 .7-.2 1z"/></svg>
          0471 592 304
        </li>
        <li class="small">
          <svg viewBox="0 0 24 24" aria-hidden="true"><rect x="2" y="5" width="20" height="14" fill="#111"/><path d="M2 5l10 8 10-8M2 19l8-7M22 19l-8-7" stroke="#fff" stroke-width="1.6" fill="none"/></svg>
          Brent.malvoy@quendix.com.au
        </li>
        <li class="small">
          <svg viewBox="0 0 24 24" aria-hidden="true"><circle cx="12" cy="12" r="10" fill="#111"/><g stroke="#fff" stroke-width="1.2" fill="none"><ellipse cx="12" cy="12" rx="4.5" ry="10"/><path d="M2 12h20M4 7h16M4 17h16M12 2v20"/></g></svg>
          www.quendix.com.au
        </li>
      </ul>
    </div>

    <svg class="card__bands" viewBox="0 0 841 32" preserveAspectRatio="none" aria-hidden="true">
      <polygon points="142,0 841,0 841,32 478,32 436,5 148,5" fill="var(--brand-blue)"/>
      <polygon points="0,16 434,16 458,32 0,32" fill="var(--accent-blue)"/>
    </svg>
  </section>
</body>
</html>
```